Sliding banner

I need three sliding banners designed for my website tillvane.co.za - please take a look at the existing banner format.

The products items on the banner can be any product that is on the website - the size of the banner must remain the same - the design project is only for the sliding banner.

Regards

```html
<!DOCTYPE html>
<html lang="en">
<head>
<meta charset="utf-8">
<title>tillvane.co.za – Sliding Banners</title>
<link href="https://fonts.googleapis.com/css2?family=Arimo:wght@400;700&display=swap" rel="stylesheet">
<style>
  :root {
    --bar: #222222;
    --page: #ffffff;
    --blue: #4a90d9;
    --blue-light: #6aaaea;
    --blue-dark: #3f84cf;
    --ink: #1e1e1e;
    --arrow-bg: #e8e8e8;
    --dot-off: #d4d4d4;
    --dot-on: #6d8fd6;
  }
  * { box-sizing: border-box; margin: 0; padding: 0; }
  html, body { width: 1127px; height: 1200px; overflow: hidden; background: var(--page); }
  body { font-family: "Arimo", Arial, sans-serif; color: var(--ink); position: relative; }
  .bar { position: absolute; left: 0; width: 1127px; background: var(--bar); }
  .slide { position: absolute; left: 0; width: 1127px; height: 380px; background: var(--page); }
  .slide > * { position: absolute; }
  .title { left: 211px; font-size: 45px; font-weight: 400; color: var(--blue); letter-spacing: -0.2px; white-space: nowrap; line-height: 1; z-index: 2; }
  .desc { left: 214px; font-size: 16px; line-height: 24px; color: var(--ink); z-index: 2; }
  .price { left: 215px; display: flex; align-items: flex-end; color: var(--blue); font-weight: 700; line-height: 1; }
  .price .only { font-size: 19px; font-weight: 400; color: var(--ink); margin-right: 8px; margin-bottom: 4px; }
  .price .cur { font-size: 26px; margin-bottom: 2px; }
  .price .amt { font-size: 50px; letter-spacing: -1px; }
  .price .cents { font-size: 25px; align-self: flex-start; margin-left: 2px; }
  .cta { left: 216px; width: 110px; height: 26px; background: linear-gradient(var(--blue-light), var(--blue-dark)); color: #fff; font-size: 13px; font-weight: 700; display: flex; align-items: center; padding-left: 11px; border-bottom: 2px solid #2f6fb5; }
  .cta svg { position: absolute; right: 8px; top: 8px; }
  .tag { background: linear-gradient(var(--blue-light), var(--blue-dark)); color: #fff; border-radius: 7px; font-size: 12px; line-height: 15px; text-align: center; display: flex; align-items: center; justify-content: center; z-index: 2; }
  .product { border-radius: 6px; z-index: 1; }
  .nav { top: 156px; width: 39px; height: 71px; background: var(--arrow-bg); display: flex; align-items: center; justify-content: center; }
  .nav.prev { left: 0; }
  .nav.next { right: 0; }
  .dots { left: 1045px; top: 343px; display: flex; gap: 10px; }
  .dot { width: 13px; height: 13px; border-radius: 50%; background: var(--dot-off); }
  .dot.active { background: var(--dot-on); }
  .brand { font-size: 12px; font-weight: 700; color: var(--blue); letter-spacing: 1px; z-index: 2; }
</style>
</head>
<body>
  <div class="bar" style="top:0;height:22px"></div>

  <section class="slide" style="top:22px">
    <h2 class="title" style="top:85px">Car Charger Dual USB</h2>
    <p class="desc" style="top:146px">This clever design gives you 2.1mA on the top USB port and<br>1mA on the bottom USB port</p>
    <div class="price" style="top:208px"><span class="only">Only</span><span class="cur">R</span><span class="amt">79</span><span class="cents">.50</span></div>
    <div class="cta" style="top:272px">GET IT NOW!<svg width="6" height="9" viewBox="0 0 6 9"><path d="M1 1l3.5 3.5L1 8" stroke="#fff" stroke-width="1.6" fill="none"/></svg></div>
    <div class="product" role="img" aria-label="White and black dual USB car charger, 3.1 amp" style="left:693px;top:84px;width:232px;height:240px;background:radial-gradient(ellipse at 60% 55%,#d9d9d9 0%,#efefef 45%,#ffffff 75%)"></div>
    <div class="tag" style="left:520px;top:233px;width:178px;height:29px;font-size:13px">Available in Black or White</div>
    <div class="nav prev"><svg width="8" height="12" viewBox="0 0 8 12"><path d="M6 1L1 6l5 5" fill="#fff"/></svg></div>
    <div class="nav next"><svg width="8" height="12" viewBox="0 0 8 12"><path d="M2 1l5 5-5 5" fill="#fff"/></svg></div>
    <div class="dots"><span class="dot active"></span><span class="dot"></span><span class="dot"></span></div>
  </section>

  <div class="bar" style="top:402px;height:10px"></div>

  <section class="slide" style="top:412px">
    <h2 class="title" style="top:89px;font-size:43px">USB to Micro USB Adaptor</h2>
    <p class="desc" style="top:150px">Turns a USB male cable into a Mini USB male<br>cable, prefect for travelling.</p>
    <div class="price" style="top:204px"><span class="only">Only</span><span class="cur">R</span><span class="amt">55</span></div>
    <div class="cta" style="top:271px">GET IT NOW!<svg width="6" height="9" viewBox="0 0 6 9"><path d="M1 1l3.5 3.5L1 8" stroke="#fff" stroke-width="1.6" fill="none"/></svg></div>
    <div class="product" role="img" aria-label="Short black USB to micro USB adaptor cable" style="left:718px;top:140px;width:226px;height:130px;background:radial-gradient(ellipse at 50% 50%,#9a9a9a 0%,#d6d6d6 40%,#ffffff 72%)"></div>
    <div class="tag" style="left:504px;top:258px;width:204px;height:40px">Compatible with Any device which<br>takes a Micro USB connector</div>
    <div class="nav prev"><svg width="8" height="12" viewBox="0 0 8 12"><path d="M6 1L1 6l5 5" fill="#fff"/></svg></div>
    <div class="nav next"><svg width="8" height="12" viewBox="0 0 8 12"><path d="M2 1l5 5-5 5" fill="#fff"/></svg></div>
    <div class="dots"><span class="dot"></span><span class="dot active"></span><span class="dot"></span></div>
  </section>

  <div class="bar" style="top:792px;height:10px"></div>

  <section class="slide" style="top:802px">
    <h2 class="title" style="top:88px">Micro USB to 30Pin Adaptor</h2>
    <p class="desc" style="top:150px">Couldn't be easier no bulky cables and no more mess!</p>
    <div class="price" style="top:182px"><span class="only">Only</span><span class="cur">R</span><span class="amt">55</span></div>
    <div class="cta" style="top:272px">GET IT NOW!<svg width="6" height="9" viewBox="0 0 6 9"><path d="M1 1l3.5 3.5L1 8" stroke="#fff" stroke-width="1.6" fill="none"/></svg></div>
    <div class="product" role="img" aria-label="White micro USB to 30-pin connector adaptor" style="left:706px;top:140px;width:226px;height:130px;background:radial-gradient(ellipse at 50% 50%,#dcdcdc 0%,#f0f0f0 45%,#ffffff 75%)"></div>
    <div class="brand" style="left:840px;top:262px">KORVEL</div>
    <div class="tag" style="left:534px;top:256px;width:204px;height:40px">Compatible with<br>Korvel Nova Tablet range</div>
    <div class="nav prev"><svg width="8" height="12" viewBox="0 0 8 12"><path d="M6 1L1 6l5 5" fill="#fff"/></svg></div>
    <div class="nav next"><svg width="8" height="12" viewBox="0 0 8 12"><path d="M2 1l5 5-5 5" fill="#fff"/></svg></div>
    <div class="dots"><span class="dot"></span><span class="dot"></span><span class="dot active"></span></div>
  </section>

  <div class="bar" style="top:1182px;height:18px"></div>
</body>
</html>
```